BrightKeel Business Card Contest

We are looking for a modern business card that catches attention and is unique. Attached is the brand guide and logo files. Please note that the back side (not the side with our name and info) with be UV raise printed, so have fun with the design there. We want to include Name, Title, Phone number, email, website.

Contact Information for Business Card

Please see project description

```html
<!DOCTYPE html>
<html lang="en">
<head>
<meta charset="UTF-8">
<title>BrightKeel Business Card</title>
<link href="https://fonts.googleapis.com/css2?family=Jost:wght@400;500;600&display=swap" rel="stylesheet">
<style>
  :root {
    --backdrop: #e4e4e6;
    --card-white: #ffffff;
    --card-navy: #323874;
    --ink-dark: #3a3d45;
    --ink-light: #ffffff;
    --mark-blue: #2f8fe0;
    --rule-red: #e8553a;
    --rule-yellow: #d8c83a;
    --rule-green: #56c06a;
    --rule-blue: #2f8fe0;
  }
  * { margin: 0; padding: 0; box-sizing: border-box; }
  html, body { width: 1200px; height: 1200px; overflow: hidden; }
  body {
    background: var(--backdrop);
    font-family: "Jost", sans-serif;
    display: flex;
    flex-direction: column;
    align-items: center;
    justify-content: center;
    gap: 80px;
  }
  .card {
    width: 700px;
    height: 400px;
    border-radius: 32px;
    position: relative;
    box-shadow: 0 18px 40px rgba(0,0,0,0.12);
  }
  .card-front {
    background: var(--card-white);
    display: flex;
    align-items: center;
    justify-content: center;
  }
  .wordmark {
    display: flex;
    align-items: center;
    gap: 18px;
  }
  .wordmark-square {
    width: 46px;
    height: 46px;
    background: var(--mark-blue);
  }
  .wordmark-name {
    font-size: 64px;
    font-weight: 500;
    color: var(--ink-dark);
    letter-spacing: -0.5px;
  }
  .card-back {
    background: var(--card-navy);
    color: var(--ink-light);
  }
  .back-mark {
    position: absolute;
    left: 70px;
    top: 70px;
    display: flex;
    align-items: center;
    gap: 12px;
  }
  .back-mark-square {
    width: 28px;
    height: 28px;
    background: var(--mark-blue);
  }
  .back-mark-name {
    font-size: 28px;
    font-weight: 500;
    color: var(--ink-light);
  }
  .person {
    position: absolute;
    left: 290px;
    top: 175px;
    width: 360px;
  }
  .person-name {
    font-size: 40px;
    font-weight: 400;
    letter-spacing: 1px;
    margin-bottom: 6px;
  }
  .person-title {
    font-size: 11px;
    font-weight: 600;
    margin-bottom: 10px;
  }
  .rainbow-rule {
    height: 1.5px;
    width: 100%;
    background: linear-gradient(90deg, var(--rule-red), var(--rule-yellow), var(--rule-green), var(--rule-blue));
    margin-bottom: 14px;
  }
  .contact-list {
    list-style: none;
    font-size: 11px;
    line-height: 1.5;
  }
</style>
</head>
<body>
  <section class="card card-front">
    <div class="wordmark">
      <span class="wordmark-square"></span>
      <span class="wordmark-name">BrightKeel</span>
    </div>
  </section>

  <section class="card card-back">
    <div class="back-mark">
      <span class="back-mark-square"></span>
      <span class="back-mark-name">BrightKeel</span>
    </div>
    <div class="person">
      <h1 class="person-name">Daniel Mwesige</h1>
      <p class="person-title">Senior UI/UX &amp; Brand Designer</p>
      <div class="rainbow-rule"></div>
      <ul class="contact-list">
        <li>+250 700 123 456</li>
        <li>daniel@brightkeel.com</li>
        <li>www.brightkeel.com</li>
      </ul>
    </div>
  </section>
</body>
</html>
```